Tease by Dusk Age Verification Landing Page

To create a visually appealing design for the landing page of the adult game "Tease by Dusk" that confirms the visitor's age.
The design should have a simple and visually appealing look that focuses on two buttons labeled "Yes" and "No". The purpose of the page is to confirm that the visitor is 18 years of age or older before accessing the game's content. Responsive design that works well on desktop and mobile devices. The final output should be delivered in PSD, AI, or Sketch format, along with any necessary images or assets.
I have also attached examples.

```html
<!DOCTYPE html>
<html lang="en">
<head>
<meta charset="utf-8">
<title>Tease by Dusk – Age Verification</title>
<link href="https://fonts.googleapis.com/css2?family=Kurale&family=Roboto:wght@400;500&display=swap" rel="stylesheet">
<style>
  :root {
    --ink: #ffffff;
    --ink-soft: #d9d2e0;
    --ink-muted: #8f8798;
    --lilac: #c9a6dc;
    --brand: #a35bc0;
    --violet: #6a35c9;
    --violet-deep: #4a2a8a;
    --card: rgba(70, 30, 80, 0.72);
    --card-mobile: rgba(110, 20, 120, 0.85);
    --night: #050308;
    --maroon: #5a0d26;
    --plum: #3b1a3c;
    --frame: rgba(255, 255, 255, 0.55);
    --dot: #8d8595;
  }
  * { margin: 0; padding: 0; box-sizing: border-box; }
  html, body { width: 944px; height: 1200px; overflow: hidden; }
  body {
    position: relative;
    background: var(--night);
    font-family: "Roboto", Arial, sans-serif;
    color: var(--ink);
  }
  .board-top {
    position: absolute; left: 0; top: 0; width: 944px; height: 712px;
    background: linear-gradient(100deg, var(--maroon) 0%, #4a1630 35%, var(--plum) 65%, #2c1a33 100%);
  }
  .board-bottom {
    position: absolute; left: 0; top: 712px; width: 944px; height: 488px;
    background:
      linear-gradient(180deg, transparent 0%, transparent 36%, rgba(40, 15, 60, 0.6) 40%, rgba(110, 10, 40, 0.7) 85%, rgba(200, 15, 35, 0.8) 100%) 490px 0 / 454px 488px no-repeat,
      linear-gradient(180deg, #000 0%, #050208 100%);
  }

  /* Screen layout (desktop units) */
  .screen {
    position: absolute; width: 852px; height: 606px; overflow: hidden;
    background: var(--night);
  }
  .screen--desktop { left: 43px; top: 44px; }
  .screen--tablet {
    left: 105px; top: 768px;
    transform: scale(0.6103); transform-origin: top left;
    border: 1.6px solid var(--frame); border-radius: 13px;
  }
  .screen__photo {
    position: absolute; inset: 0;
    background:
      linear-gradient(90deg, transparent 60%, rgba(30, 40, 140, 0.5) 74%, rgba(10, 10, 30, 0.2) 82%, rgba(120, 20, 50, 0.5) 92%, rgba(210, 15, 30, 0.9) 100%),
      linear-gradient(160deg, #0a0710 0%, #2a1626 35%, #3a1e30 55%, #160a18 75%, #2a0c22 100%);
  }
  .screen__shade {
    position: absolute; inset: 0;
    background: linear-gradient(90deg, transparent 40%, rgba(0, 0, 0, 0.75) 60%, rgba(0, 0, 0, 0.55) 85%, transparent 100%);
  }
  .brand {
    position: absolute; left: 24px; top: 30px;
    display: flex; align-items: center; gap: 8px;
    font-family: "Kurale", Georgia, serif; font-size: 24px; color: var(--brand);
  }
  .brand__dot { width: 14px; height: 14px; border-radius: 50%; background: var(--ink); }
  .sound {
    position: absolute; left: 782px; top: 18px; width: 30px; height: 30px;
    border: 1.5px solid #9a93a2; border-radius: 50%;
    display: flex; align-items: center; justify-content: center;
    background: rgba(255, 255, 255, 0.08);
  }
  .welcome { position: absolute; left: 502px; top: 100px; font-family: "Kurale", Georgia, serif; }
  .welcome__title { font-size: 42px; line-height: 48px; font-weight: 400; color: var(--ink); }
  .welcome__sub { font-size: 22px; line-height: 26px; color: var(--lilac); }
  .intro {
    position: absolute; left: 502px; top: 187px; width: 282px;
    font-size: 10.7px; line-height: 15px; color: var(--ink);
  }
  .age-card {
    position: absolute; left: 502px; top: 269px; width: 277px; height: 131px;
    background: var(--card);
  }
  .age-card__title { position: absolute; left: 16px; top: 16px; font-size: 18.5px; font-weight: 500; white-space: nowrap; }
  .age-card__text { position: absolute; left: 16px; top: 53px; width: 250px; font-size: 9.5px; line-height: 13px; }
  .age-card__actions { position: absolute; left: 0; bottom: 0; width: 100%; height: 27px; display: flex; }
  .btn { flex: 1; display: flex; align-items: center; justify-content: center; font-size: 10.5px; color: var(--ink); }
  .btn--yes { background: var(--violet); flex: 0 0 136px; }
  .btn--no { background: var(--violet-deep); }
  .notice {
    position: absolute; left: 505px; top: 425px; width: 250px;
    display: flex; gap: 5px; font-size: 9.5px; line-height: 13px; color: var(--ink-muted);
  }
  .notice svg { flex: none; margin-top: 1px; }
  .footer-nav {
    position: absolute; left: 0; right: 0; top: 578px;
    display: flex; justify-content: center; align-items: center;
    font-size: 10.6px; color: var(--ink-soft);
  }
  .footer-nav__sep { width: 4px; height: 4px; border-radius: 50%; background: var(--dot); margin: 0 23px; }

  /* Mobile screen */
  .phone {
    position: absolute; left: 680px; top: 794px; width: 153px; height: 294px; overflow: hidden;
    border: 1px solid var(--frame); border-radius: 4px; background: var(--night);
  }
  .phone__photo {
    position: absolute; inset: 0;
    background:
      linear-gradient(90deg, transparent 70%, rgba(90, 50, 80, 0.45) 100%),
      linear-gradient(180deg, #050308 0%, #0c0610 60%, #1a0a16 100%);
  }
  .phone .brand { left: 14px; top: 13px; font-size: 8px; gap: 3px; }
  .phone .brand__dot { width: 6px; height: 6px; }
  .phone .sound { left: 123px; top: 11px; width: 18px; height: 18px; border-width: 1px; }
  .phone .welcome { left: 11px; top: 55px; }
  .phone .welcome__title { font-size: 20px; line-height: 22px; }
  .phone .welcome__sub { font-size: 10.5px; line-height: 13px; }
  .phone .age-card { left: 10px; top: 112px; width: 133px; height: 79px; background: var(--card-mobile); }
  .phone .age-card__title { left: 8px; top: 9px; font-size: 11.5px; }
  .phone .age-card__text { left: 8px; top: 32px; width: 124px; font-size: 5.6px; line-height: 8px; }
  .phone .age-card__actions { height: 16px; }
  .phone .btn { font-size: 6px; }
  .phone .btn--yes { flex: 0 0 66px; }
  .phone .notice { left: 7px; top: 209px; width: 138px; gap: 3px; font-size: 5.3px; line-height: 8px; }
  .phone .footer-nav { top: 272px; font-size: 6.3px; }
  .phone .footer-nav__sep { width: 2px; height: 2px; margin: 0 5px; }
</style>
</head>
<body>
  <div class="board-top"></div>
  <div class="board-bottom" role="img" aria-label="Blurred neon club backdrop"></div>

  <!-- Desktop -->
  <section class="screen screen--desktop">
    <div class="screen__photo" role="img" aria-label="Blurred photo of a dancer seated beside a pole in a neon-lit club"></div>
    <div class="screen__shade"></div>
    <div class="brand"><span class="brand__dot"></span>Tease by Dusk</div>
    <div class="sound">
      <svg width="16" height="14" viewBox="0 0 16 14"><path d="M1 5h3l4-3v10l-4-3H1z" fill="#fff"/><path d="M10 4.5a3 3 0 0 1 0 5" stroke="#fff" stroke-width="1.2" fill="none"/><path d="M12 2.5a5.5 5.5 0 0 1 0 9" stroke="#fff" stroke-width="1.2" fill="none"/></svg>
    </div>
    <div class="welcome">
      <h1 class="welcome__title">Welcome</h1>
      <p class="welcome__sub">to Tease by Dusk</p>
    </div>
    <p class="intro">Before you get started, we need to confirm your age. Our content is intended for a mature audience and is not suitable for individuals under 18.</p>
    <div class="age-card">
      <h2 class="age-card__title">Are You 18+ Years Old?</h2>
      <p class="age-card__text">Please confirm that you are 18 years or older by clicking the "Yes" button below.</p>
      <div class="age-card__actions"><span class="btn btn--yes">YES</span><span class="btn btn--no">NO</span></div>
    </div>
    <p class="notice">
      <svg width="11" height="11" viewBox="0 0 12 12"><circle cx="6" cy="6" r="6" fill="#8f8798"/><rect x="5.3" y="5" width="1.4" height="4" fill="#111"/><circle cx="6" cy="3.4" r="0.8" fill="#111"/></svg>
      <span>By clicking "Yes", you acknowledge that you are fully aware of the explicit nature of the content provided in Tease and are of legal age to access it.</span>
    </p>
    <nav class="footer-nav"><span>About Us</span><i class="footer-nav__sep"></i><span>FAQ</span><i class="footer-nav__sep"></i><span>Contact Us</span><i class="footer-nav__sep"></i><span>Terms of Service</span><i class="footer-nav__sep"></i><span>Privacy Policy</span></nav>
  </section>

  <!-- Tablet -->
  <section class="screen screen--tablet">
    <div class="screen__photo" role="img" aria-label="Blurred photo of a dancer seated beside a pole in a neon-lit club"></div>
    <div class="screen__shade"></div>
    <div class="brand"><span class="brand__dot"></span>Tease by Dusk</div>
    <div class="sound">
      <svg width="16" height="14" viewBox="0 0 16 14"><path d="M1 5h3l4-3v10l-4-3H1z" fill="#fff"/><path d="M10 4.5a3 3 0 0 1 0 5" stroke="#fff" stroke-width="1.2" fill="none"/><path d="M12 2.5a5.5 5.5 0 0 1 0 9" stroke="#fff" stroke-width="1.2" fill="none"/></svg>
    </div>
    <div class="welcome">
      <h1 class="welcome__title">Welcome</h1>
      <p class="welcome__sub">to Tease by Dusk</p>
    </div>
    <p class="intro">Before you get started, we need to confirm your age. Our content is intended for a mature audience and is not suitable for individuals under 18.</p>
    <div class="age-card">
      <h2 class="age-card__title">Are You 18+ Years Old?</h2>
      <p class="age-card__text">Please confirm that you are 18 years or older by clicking the "Yes" button below.</p>
      <div class="age-card__actions"><span class="btn btn--yes">YES</span><span class="btn btn--no">NO</span></div>
    </div>
    <p class="notice">
      <svg width="11" height="11" viewBox="0 0 12 12"><circle cx="6" cy="6" r="6" fill="#8f8798"/><rect x="5.3" y="5" width="1.4" height="4" fill="#111"/><circle cx="6" cy="3.4" r="0.8" fill="#111"/></svg>
      <span>By clicking "Yes", you acknowledge that you are fully aware of the explicit nature of the content provided in Tease and are of legal age to access it.</span>
    </p>
    <nav class="footer-nav"><span>About Us</span><i class="footer-nav__sep"></i><span>FAQ</span><i class="footer-nav__sep"></i><span>Contact Us</span><i class="footer-nav__sep"></i><span>Terms of Service</span><i class="footer-nav__sep"></i><span>Privacy Policy</span></nav>
  </section>

  <!-- Mobile -->
  <section class="phone">
    <div class="phone__photo" role="img" aria-label="Blurred photo of a dancer at the right edge of a dark club"></div>
    <div class="brand"><span class="brand__dot"></span>Tease by Dusk</div>
    <div class="sound">
      <svg width="10" height="9" viewBox="0 0 16 14"><path d="M1 5h3l4-3v10l-4-3H1z" fill="#fff"/><path d="M10 4.5a3 3 0 0 1 0 5" stroke="#fff" stroke-width="1.4" fill="none"/><path d="M12 2.5a5.5 5.5 0 0 1 0 9" stroke="#fff" stroke-width="1.4" fill="none"/></svg>
    </div>
    <div class="welcome">
      <h1 class="welcome__title">Welcome</h1>
      <p class="welcome__sub">to Tease by Dusk</p>
    </div>
    <div class="age-card">
      <h2 class="age-card__title">Are You 18+ Years Old?</h2>
      <p class="age-card__text">Please confirm that you are 18 years or older by clicking the "Yes" button below.</p>
      <div class="age-card__actions"><span class="btn btn--yes">YES</span><span class="btn btn--no">NO</span></div>
    </div>
    <p class="notice">
      <svg width="6" height="6" viewBox="0 0 12 12"><circle cx="6" cy="6" r="6" fill="#8f8798"/><rect x="5.3" y="5" width="1.4" height="4" fill="#111"/><circle cx="6" cy="3.4" r="0.8" fill="#111"/></svg>
      <span>By clicking "Yes", you acknowledge that you are fully aware of the explicit nature of the content provided in Tease and are of legal age to access it.</span>
    </p>
    <nav class="footer-nav"><span>About Us</span><i class="footer-nav__sep"></i><span>FAQ</span><i class="footer-nav__sep"></i><span>Contact Us</span><i class="footer-nav__sep"></i><span>Terms</span></nav>
  </section>
</body>
</html>
```